Ridge Contracting LLC Business Card Design

I am looking for a creative and unique business card design. We are a commercial construction general contractor. With the name "RIDGE" Contracting, I am hoping to see some neat designs that correlate with the name.

```html
<!DOCTYPE html>
<html lang="en">
<head>
<meta charset="utf-8">
<title>Ridge Contracting LLC Business Card</title>
<link href="https://fonts.googleapis.com/css2?family=Montserrat:wght@400;500;700;800&display=swap" rel="stylesheet">
<style>
  :root {
    --stage: #3a3a3a;
    --blue: #1f86cf;
    --blue-light: #2fa3e0;
    --grey: #b9b9bb;
    --ink: #1b1b1b;
    --white: #ffffff;
  }
  * { box-sizing: border-box; margin: 0; padding: 0; }
  html, body { width: 1200px; height: 689px; overflow: hidden; }
  body {
    background: var(--stage);
    font-family: "Montserrat", sans-serif;
    display: flex;
    align-items: center;
    justify-content: center;
    gap: 60px;
  }
  .card {
    position: relative;
    width: 520px;
    height: 297px;
    border-radius: 18px;
    overflow: hidden;
  }
  .card--front {
    background: radial-gradient(circle at 40% 35%, var(--blue-light), var(--blue));
    display: flex;
    align-items: center;
    justify-content: center;
  }
  .brand {
    display: flex;
    align-items: center;
    gap: 10px;
    font-weight: 800;
    letter-spacing: 1px;
    white-space: nowrap;
  }
  .brand__dot { width: 18px; height: 18px; border-radius: 50%; flex: none; }
  .card--front .brand { color: var(--white); font-size: 38px; }
  .card--front .brand__dot { background: var(--white); }

  .card--back { background: var(--white); }
  .card--back .brand {
    position: absolute; top: 80px; right: 24px;
    color: var(--blue); font-size: 18px;
  }
  .card--back .brand__dot { background: var(--blue); width: 12px; height: 12px; }

  .contact { position: absolute; left: 34px; top: 30px; color: var(--ink); }
  .contact__name { color: var(--blue); font-weight: 700; font-size: 20px; letter-spacing: 0.5px; line-height: 1.2; }
  .contact__role { font-size: 12px; margin-top: 2px; }
  .contact__address { font-size: 12px; line-height: 1.4; margin-top: 14px; }
  .contact__list { list-style: none; margin-top: 12px; font-size: 12px; line-height: 1.6; }
  .contact__list li { display: flex; align-items: center; gap: 8px; }
  .contact__list svg { width: 11px; height: 11px; fill: var(--blue); flex: none; }

  .swoosh { position: absolute; left: 0; top: 0; width: 520px; height: 297px; }
  .tagline {
    position: absolute; left: 40px; bottom: 10px;
    color: var(--white); font-size: 14px; font-weight: 500; letter-spacing: 0.5px;
  }
</style>
</head>
<body>
  <section class="card card--front">
    <div class="brand"><span class="brand__dot"></span>RIDGE CONTRACTING</div>
  </section>

  <section class="card card--back">
    <svg class="swoosh" viewBox="0 0 520 297" aria-hidden="true">
      <path d="M0 245 C220 230 420 190 520 125 L520 150 C420 215 220 250 0 262 Z" fill="var(--grey)"/>
      <path d="M0 262 C220 250 420 215 520 150 L520 297 L0 297 Z" fill="var(--blue)"/>
      <path d="M200 244 C330 230 440 192 512 140" stroke="var(--white)" stroke-width="2.5" fill="none"/>
    </svg>

    <div class="contact">
      <h1 class="contact__name">DARREN HOLLOWAY</h1>
      <p class="contact__role">Managing director</p>
      <p class="contact__address">2450 Harlow St, Ste<br>210, Dalton, TX 75204</p>
      <ul class="contact__list">
        <li><svg viewBox="0 0 12 12"><path d="M2 1h3l1 3-2 1a7 7 0 0 0 3 3l1-2 3 1v3c0 .6-.4 1-1 1A10 10 0 0 1 1 2c0-.6.4-1 1-1z"/></svg>555-314-2087</li>
        <li><svg viewBox="0 0 12 12"><path d="M0 2h12v8H0z M0 2l6 5 6-5" stroke="#fff" stroke-width="1"/></svg>info@ridgebuilds.com</li>
        <li><svg viewBox="0 0 12 12"><circle cx="6" cy="6" r="6"/></svg>www.ridgebuilds.com</li>
      </ul>
    </div>

    <div class="brand"><span class="brand__dot"></span>RIDGE CONTRACTING</div>

    <p class="tagline">"RIDGE" Contracting</p>
  </section>
</body>
</html>
```